New web design needed for our company

We need our website designing, it needs to be professional and look creative,
We are a plumbing and heating company called Kestrel Bay's (www.kestrelbays.co.uk)
I like this site design also some of the following maybe:
https://www.marnockheating.com/
http://www.tavelpower.co.uk

Please let me know when you want our logo files as it wont let me upload them

The design will require coding once the design is complete, i havent paid for this yet as i want to be sure the design is good before i commit.

The template needs to look professional and look like one of the leading companies.
The site will consist of all the features this site has https://www.marnockheating.com/

I like a modern design with the latest technology.

Must have a customer login page and a my account area

Target Market(s)

Everyone

Industry/Entity Type

Plumbing

Coding

Coded - Design and coding required

Number of Pages Required

5+ page

Font styles to use
Other font styles liked:
• whatever suites

Requirements
Must have
• The design will require coding once the design is complete, i havent paid for this yet as i want to be sure the design is good before i commit.
• The template needs to look professional and look like one of the leading companies.
• The site will consist of all the features this site has https://www.marnockheating.com/
• I like a modern design with the latest technology.
• Must have a customer login page and a my account area
Nice to have
• inspirational and different
Should not have
• plain boring designs like most plumbing websites, needs to be inspiring and attract people from first sight.

```html
<!DOCTYPE html>
<html lang="en">
<head>
<meta charset="utf-8">
<title>Kestrel Bay's – Your Local Experts</title>
<link href="https://fonts.googleapis.com/css2?family=Poppins:wght@400;500;600;700&family=Open+Sans:wght@400;600&display=swap" rel="stylesheet">
<style>
:root{
  --blue:#2c5699;
  --blue-dark:#1f3e73;
  --orange:#f1573b;
  --ink:#2a2a2a;
  --muted:#8a8a8a;
  --light:#f4f4f4;
  --footer:#242424;
  --footer-deep:#191919;
  --white:#fff;
}
*{box-sizing:border-box;margin:0;padding:0}
html,body{width:1200px;height:3315px;overflow:hidden}
body{position:relative;background:var(--white);font-family:'Open Sans',Arial,sans-serif;color:var(--ink)}
.abs{position:absolute}
.heading{font-family:'Poppins',Arial,sans-serif;font-weight:600;color:var(--ink)}
.rule{position:absolute;height:4px;width:44px;background:var(--orange)}

/* top bar */
.topbar{top:0;left:0;width:1200px;height:40px;border-bottom:1px solid #e6e6e6;font-family:'Poppins',sans-serif;font-size:12px}
.topbar .links{position:absolute;left:80px;top:12px;display:flex;gap:20px;color:#555}
.topbar .links b{color:var(--ink)}
.topbar .links b span{color:var(--blue)}
.topbar .social{position:absolute;left:884px;top:13px;display:flex;gap:13px}
.topbar .social i{width:13px;height:13px;border-radius:50%;background:#555;display:block}
.topbar .lang{position:absolute;left:1040px;top:12px;color:#555;display:flex;align-items:center;gap:6px}
.topbar .lang i{width:16px;height:11px;background:#3b5fa8;display:block}

/* header */
.logo{position:absolute;left:80px;top:62px;font-family:'Poppins',sans-serif;font-weight:700;font-size:44px;color:var(--blue);line-height:1;letter-spacing:-1px}
.tagline{position:absolute;left:168px;top:118px;font-family:'Poppins',sans-serif;font-size:14px;color:var(--blue)}
.info{position:absolute;top:80px;display:flex;gap:14px;font-family:'Poppins',sans-serif}
.info .ring{width:42px;height:42px;border:2px solid #444;border-radius:50%;display:flex;align-items:center;justify-content:center}
.info h4{font-size:13px;font-weight:600;margin-top:4px}
.info h4 strong{font-size:16px;margin-left:8px;letter-spacing:1px}
.info p{font-size:11px;color:#666;margin-top:4px}

/* nav */
.nav{top:161px;left:0;width:1200px;height:56px;background:var(--blue)}
.nav a{position:absolute;top:19px;font-family:'Poppins',sans-serif;font-size:14px;color:var(--white);text-decoration:none}
.nav a.active{color:var(--orange)}
.nav .cta{position:absolute;left:932px;top:0;width:188px;height:56px;background:var(--blue-dark);color:var(--white);font-family:'Poppins',sans-serif;font-size:12px;font-weight:500;display:flex;align-items:center;justify-content:center;letter-spacing:.3px}

/* hero */
.hero{top:217px;left:0;width:1200px;height:545px;background:linear-gradient(100deg,#2d5ea8 0%,#4f7fc2 35%,#c9d3dd 65%,#8e969e 100%)}
.hero .arrow{position:absolute;top:262px;width:14px;height:22px}

/* account */
.account-card{position:absolute;top:906px;width:330px;height:239px}
.account-card .photo{height:186px}
.account-card .label{height:53px;background:var(--blue);color:var(--white);font-family:'Poppins',sans-serif;font-weight:600;font-size:21px;display:flex;align-items:center;justify-content:center}

/* services */
.service{position:absolute;width:330px}
.service svg{position:absolute;left:0;top:0}
.service h3{position:absolute;left:73px;top:0;font-family:'Poppins',sans-serif;font-weight:600;font-size:16px;white-space:nowrap}
.service p{position:absolute;left:73px;top:32px;width:250px;font-size:12px;line-height:22px;color:var(--muted)}

/* financial */
.finance-photo{top:1695px;left:0;width:599px;height:570px;background:linear-gradient(135deg,#2b4f93 0%,#5b6f8c 45%,#c4c6c8 70%,#c3342f 100%)}
.finance-panel{top:1695px;left:599px;width:601px;height:570px;background:var(--light)}
.finance-panel h2{position:absolute;left:104px;top:106px;font-family:'Poppins',sans-serif;font-weight:600;font-size:36px}
.finance-panel .sub{position:absolute;left:104px;top:158px;font-family:'Poppins',sans-serif;font-weight:500;font-size:15px;color:var(--blue)}
.finance-panel p{position:absolute;left:104px;top:208px;width:472px;font-size:13px;line-height:24px;color:#777}
.btn{position:absolute;background:var(--blue);color:var(--white);font-family:'Poppins',sans-serif;font-weight:500;font-size:13px;display:flex;align-items:center;justify-content:center}

/* testimonials */
.testimonial{position:absolute;top:2435px;width:520px;height:180px}
.testimonial .avatar{position:absolute;left:0;top:0;width:132px;height:133px}
.testimonial p{position:absolute;left:159px;top:0;width:350px;font-family:'Poppins',sans-serif;font-size:14px;line-height:25px;color:#555}
.testimonial h5{position:absolute;left:159px;top:131px;font-family:'Poppins',sans-serif;font-weight:600;font-size:15px;color:var(--blue)}
.testimonial span{position:absolute;left:159px;top:158px;font-family:'Poppins',sans-serif;font-size:12px;color:#666}
.dots{position:absolute;top:2638px;left:578px;display:flex;gap:5px}
.dots i{width:10px;height:10px;border:1px solid #999;border-radius:50%;display:block}
.dots i.on{border:2px solid #444}

/* call to action */
.cta-band{top:2736px;left:0;width:1200px;height:144px;background:var(--blue)}
.cta-band h2{position:absolute;left:80px;top:46px;font-family:'Poppins',sans-serif;font-weight:600;font-size:30px;color:var(--white)}
.cta-band p{position:absolute;left:80px;top:88px;font-family:'Poppins',sans-serif;font-size:14px;color:#b9c8e2}
.cta-band .field{position:absolute;left:703px;top:50px;width:302px;height:46px;background:var(--white);font-family:'Poppins',sans-serif;font-size:11px;color:#aaa;padding:15px 18px}
.cta-band .send{position:absolute;left:1005px;top:50px;width:115px;height:46px;background:var(--orange)}

/* footer */
.footer{top:2880px;left:0;width:1200px;height:364px;background:var(--footer);font-family:'Poppins',sans-serif}
.footer .brand{position:absolute;left:80px;top:66px;font-weight:700;font-size:40px;color:var(--blue);letter-spacing:-1px;line-height:1}
.footer .about{position:absolute;left:80px;top:140px;width:300px;font-size:12px;line-height:22px;color:#6f6f6f}
.footer .contact{position:absolute;left:80px;color:#ccc}
.footer h4{position:absolute;top:76px;font-weight:600;font-size:17px;color:var(--white)}
.footer .col-rule{position:absolute;top:107px;width:30px;height:3px;background:var(--orange)}
.footer ul{position:absolute;top:142px;list-style:none;font-size:12px;color:#8c8c8c}
.footer li{height:30px;display:flex;align-items:center;gap:14px}
.footer li i{width:10px;height:10px;background:#8c8c8c;border-radius:50%;display:block}
.footer li b{font-weight:400;color:#8c8c8c}
.footer .hours p{font-size:12px;line-height:22px;color:#8c8c8c;width:240px}
.footer .hours .row{display:flex;justify-content:space-between;width:240px;font-size:12px;color:#aaa;height:30px;align-items:center}
.bottom{top:3244px;left:0;width:1200px;height:71px;background:var(--footer-deep);font-family:'Poppins',sans-serif;font-size:13px;color:#ccc}
.bottom .copy{position:absolute;width:1200px;text-align:center;top:26px}
.bottom .back{position:absolute;left:1042px;top:27px;font-size:11px;color:#888;letter-spacing:.5px}
</style>
</head>
<body>

<header>
  <div class="abs topbar">
    <div class="links"><b>Welcome to <span>Kestrel Bay's</span></b><span>Email Us</span><span>How to Find Us</span><span>Give Feedback</span></div>
    <div class="social"><i></i><i></i><i></i><i></i><i></i></div>
    <div class="lang"><i></i>English ▾</div>
  </div>

  <div class="logo">Kestrel Bay's</div>
  <div class="tagline">Your Local Experts</div>

  <div class="info" style="left:515px">
    <div class="ring"><svg width="16" height="20" viewBox="0 0 16 20"><path d="M8 1a6 6 0 0 0-6 6c0 5 6 12 6 12s6-7 6-12a6 6 0 0 0-6-6z" fill="#444"/><circle cx="8" cy="7" r="2.2" fill="#fff"/></svg></div>
    <div><h4>Call Today<strong>08175529</strong></h4><p>28 Harrow Lane, Fairview W4 2LR</p></div>
  </div>
  <div class="info" style="left:843px">
    <div class="ring"><svg width="20" height="20" viewBox="0 0 20 20"><circle cx="10" cy="10" r="7" fill="none" stroke="#444" stroke-width="2"/><path d="M10 6v4l3 2" fill="none" stroke="#444" stroke-width="2"/></svg></div>
    <div><h4>Open Hours</h4><p>Mon – Sat: 8 am – 5 pm, Sunday: CLOSED</p></div>
  </div>

  <nav class="abs nav">
    <a class="active" style="left:100px">Home</a>
    <a style="left:195px">My Account</a>
    <a style="left:327px">Services</a>
    <a style="left:437px">Emergencies</a>
    <a style="left:579px">Business</a>
    <a style="left:694px">Customers</a>
    <div class="cta">GET AN APPOINTMENT</div>
  </nav>
</header>

<section class="abs hero" role="img" aria-label="Smiling plumber in blue uniform fitting pipework under a sink">
  <svg class="arrow" style="left:40px" viewBox="0 0 14 22"><path d="M12 2 3 11l9 9" fill="none" stroke="rgba(255,255,255,.5)" stroke-width="2"/></svg>
  <svg class="arrow" style="left:1130px" viewBox="0 0 14 22"><path d="m2 2 9 9-9 9" fill="none" stroke="rgba(255,255,255,.5)" stroke-width="2"/></svg>
</section>

<section class="account">
  <h2 class="abs heading" style="left:80px;top:807px;font-size:32px">My Account</h2>
  <div class="account-card" style="left:80px">
    <div class="photo" role="img" aria-label="Hands at a laptop with financial charts on the desk" style="background:linear-gradient(135deg,#e8e8e8,#9fb3cf 60%,#3a3a3a)"></div>
    <div class="label">Payments</div>
  </div>
  <div class="account-card" style="left:435px">
    <div class="photo" role="img" aria-label="Businessman in a suit with digital certificate graphics" style="background:linear-gradient(135deg,#2f3d55,#4f7fb5 55%,#1c2434)"></div>
    <div class="label">Manage Certificates</div>
  </div>
  <div class="account-card" style="left:791px">
    <div class="photo" role="img" aria-label="Hand holding a small model house and keys" style="background:linear-gradient(135deg,#e9e6e2,#d9b79c 55%,#b5493a)"></div>
    <div class="label">Manage Properties</div>
  </div>
</section>

<section class="services">
  <h2 class="abs heading" style="left:80px;top:1203px;font-size:30px">Our Services</h2>
  <div class="rule" style="left:80px;top:1258px"></div>

  <div class="service" style="left:80px;top:1322px">
    <svg width="34" height="40" viewBox="0 0 34 40"><rect x="3" y="5" width="28" height="33" fill="none" stroke="#2c5699" stroke-width="2.5"/><rect x="11" y="1" width="12" height="7" fill="#2c5699"/><path d="M9 17h16M9 24h16M9 31h10" stroke="#2c5699" stroke-width="2.5"/></svg>
    <h3>Combi Boiler Installation</h3>
    <p>Sed ut perspiciatis unde omnis iste error sit voluptatem accusantium doloremque lau dantium, rem aperiam eaque ipsa ab illo inventore veritatis</p>
  </div>
  <div class="service" style="left:435px;top:1322px">
    <svg width="40" height="30" viewBox="0 0 40 30"><path d="M2 26 14 13l8 7L37 5" fill="none" stroke="#2c5699" stroke-width="3.5"/><path d="M27 4h11v11" fill="none" stroke="#2c5699" stroke-width="3.5"/></svg>
    <h3>Regular Boiler Installation</h3>
    <p>Sed ut perspiciatis unde omnis iste error sit voluptatem accusantium doloremque lau dantium, rem aperiam eaque ipsa ab illo inventore veritatis</p>
  </div>
  <div class="service" style="left:791px;top:1322px">
    <svg width="40" height="40" viewBox="0 0 40 40"><circle cx="20" cy="22" r="14" fill="none" stroke="#2c5699" stroke-width="3"/><path d="M20 14v9l6 4M4 8l7-5M36 8l-7-5" fill="none" stroke="#2c5699" stroke-width="3"/></svg>
    <h3>Replace a System Boiler</h3>
    <p>Sed ut perspiciatis unde omnis iste error sit voluptatem accusantium doloremque lau dantium, rem aperiam eaque ipsa ab illo inventore veritatis</p>
  </div>
  <div class="service" style="left:80px;top:1512px">
    <svg width="40" height="40" viewBox="0 0 40 40"><path d="M4 36 24 16" stroke="#2c5699" stroke-width="4"/><path d="M28 3v6M35 12h-6M34 5l-4 4M20 6l2 4M32 22l-4-2" stroke="#2c5699" stroke-width="2.5"/></svg>
    <h3>System Boiler Installation</h3>
    <p>Sed ut perspiciatis unde omnis iste error sit voluptatem accusantium doloremque lau dantium, rem aperiam eaque ipsa ab illo inventore veritatis</p>
  </div>
  <div class="service" style="left:435px;top:1512px">
    <svg width="42" height="40" viewBox="0 0 42 40"><rect x="3" y="8" width="36" height="24" fill="none" stroke="#2c5699" stroke-width="3"/><rect x="9" y="14" width="24" height="12" fill="#2c5699"/><path d="M16 2l5 6 5-6M10 38l4-6M32 38l-4-6" fill="none" stroke="#2c5699" stroke-width="2.5"/></svg>
    <h3>Replace a Combi Boiler</h3>
    <p>Sed ut perspiciatis unde omnis iste error sit voluptatem accusantium doloremque lau dantium, rem aperiam eaque ipsa ab illo inventore veritatis</p>
  </div>
  <div class="service" style="left:791px;top:1512px">
    <svg width="40" height="40" viewBox="0 0 40 40"><circle cx="20" cy="20" r="17" fill="#2c5699"/><path d="M9 12c5 1 6 5 10 4s3 7 7 8M26 6c-2 4 2 6 6 7M14 30c2-4 6-4 7-2" fill="none" stroke="#fff" stroke-width="2.5"/></svg>
    <h3>Replace a Regular boiler</h3>
    <p>Sed ut perspiciatis unde omnis iste error sit voluptatem accusantium doloremque lau dantium, rem aperiam eaque ipsa ab illo inventore veritatis</p>
  </div>
</section>

<section class="financial">
  <div class="abs finance-photo" role="img" aria-label="Engineer in blue overalls repairing an appliance with tools from a red toolbox"></div>
  <div class="abs finance-panel">
    <h2>Financial Experts</h2>
    <div class="sub">providing the best financial consultants</div>
    <p>Sed ut perspiciatis unde omnis iste natus error sit voluptatem accusantium doloremque laudantium, totam rem aperiam, eaque ipsa quae ab illo inventore veritatis et quasi architecto beatae vitae dicta sunt explicabo. Nemo enim ipsam voluptatem quia voluptas sit aspernatur aut odit aut fugit, sed quia consequuntur magni dolores eos qui ratione voluptatem sequi nesciunt, neque porro quisquam est</p>
    <div class="btn" style="left:104px;top:415px;width:125px;height:43px">Read More</div>
  </div>
</section>

<section class="clients">
  <h2 class="abs heading" style="left:0;width:1200px;text-align:center;top:2314px;font-size:32px">1000+ Happy Clients</h2>
  <div class="rule" style="left:578px;top:2370px"></div>

  <div class="testimonial" style="left:80px">
    <div class="avatar" role="img" aria-label="Portrait of a customer in a dark suit" style="background:linear-gradient(135deg,#d9d6d1,#6f6a64)"></div>
    <p>Lumen Themes produces high quality themes and they provide support excellent support if you run into any problems. I recommend this template without hesitation!</p>
    <h5>Daniel Ashworth</h5>
    <span>Customer Service</span>
  </div>
  <div class="testimonial" style="left:614px">
    <div class="avatar" role="img" aria-label="Portrait of a customer in a light shirt" style="background:linear-gradient(135deg,#e4e4e2,#a9a6a0)"></div>
    <p>Lumen Themes produces high quality themes and they provide support excellent support if you run into any problems. I recommend this template without hesitation!</p>
    <h5>Oliver Brandt</h5>
    <span>Human Resources</span>
  </div>
  <div class="dots"><i></i><i></i><i class="on"></i></div>
</section>

<section class="abs cta-band">
  <h2>Need more information?</h2>
  <p>We can call you and help with your problem, just leave us your phone number.</p>
  <div class="field">Enter you email...</div>
  <div class="send"></div>
</section>

<footer class="abs footer">
  <div class="brand">Kestrel Bay's</div>
  <p class="about">Lorem ipsum dolor sit consectetur adipiscing elit sed do eiusmod tempor incididunt ut labore et dolore magna veniam aliqua.</p>
  <div class="contact" style="top:232px;display:flex;align-items:center;gap:28px">
    <svg width="16" height="16" viewBox="0 0 16 16"><path d="M3 1l3 1 1 4-2 1c1 2 3 4 5 5l1-2 4 1 1 3-2 2C8 15 1 8 1 3z" fill="#2c5699"/></svg>
    <span style="font-size:21px;letter-spacing:4px">08175529</span>
  </div>
  <div class="contact" style="top:265px;left:124px;font-size:16px">mail@kestrelbays.co.uk</div>

  <h4 style="left:435px">Follow us</h4><div class="col-rule" style="left:435px"></div>
  <ul style="left:435px">
    <li><i></i>Newsfeed</li><li><i></i>Updates</li><li><i></i>Community</li><li><i></i>Network</li><li><i></i>Videos</li>
  </ul>

  <h4 style="left:659px">Our services</h4><div class="col-rule" style="left:659px"></div>
  <ul style="left:659px">
    <li><b>›</b>Accumulation</li><li><b>›</b>Taxation</li><li><b>›</b>Risk Management</li><li><b>›</b>Estate Planning</li><li><b>›</b>Business Planning</li>
  </ul>

  <h4 style="left:882px">Business hours</h4><div class="col-rule" style="left:882px"></div>
  <div class="hours abs" style="left:882px;top:142px">
    <p>Our suppoer available to help you 24 hours a day, seven days week</p>
    <div class="row" style="margin-top:8px"><span>Monday–Saturday: ..............</span><span>8.00–18.00</span></div>
    <div class="row"><span>Sunday: ...............................</span><span>Closed</span></div>
    <div class="row"><span>Calendar Events: ...................</span><span>Closed</span></div>
  </div>
</footer>

<div class="abs bottom">
  <div class="copy">Copyright © &nbsp;All Rights Reserved</div>
  <div class="back">BACK TOP &nbsp;<span style="color:var(--blue)">↑</span></div>
</div>

</body>
</html>
```